Bref créative
MOBILE ULTRASOUND BUSINESS
Professional
Nora K. Pellway Hussel
President and Director of Ultrasound
517 Thornbury Lane #2614
Millbrook Twp. PA. 15832
nora@keystonepulsescanworks.example
keystonepulsescanworks.example
We need business cards for my husband as well, all info will be the same except for his name is Gavin P. Hussel - Chief Operating Officer for title - and gavin@keystonepulsescanworks.example
vector logo file

```html
<!DOCTYPE html>
<html lang="en">
<head>
<meta charset="utf-8">
<title>Keystone Pulse Scan Works – Business Cards</title>
<link href="https://fonts.googleapis.com/css2?family=PT+Serif:wght@400;700&display=swap" rel="stylesheet">
<style>
  :root{
    --page:#e9e6e1;
    --card-light:#ffffff;
    --card-dark:#1f1f21;
    --blue-top:#5fb4ec;
    --blue-mid:#1f87d6;
    --blue-deep:#0b5fae;
    --green:#5aa83a;
    --logo-blue:#1a6fc0;
    --logo-green:#4c9a2e;
    --ink-light:#ffffff;
  }
  *{box-sizing:border-box;margin:0;padding:0}
  html,body{width:1200px;height:852px;overflow:hidden}
  body{background:var(--page);font-family:"PT Serif",Georgia,serif;position:relative}

  .card{
    position:absolute;width:520px;height:298px;border-radius:16px;overflow:hidden;
    box-shadow:0 10px 24px rgba(0,0,0,.25);
    display:flex;flex-direction:column;
  }
  .card--light{left:50px;top:277px;background:var(--card-light)}
  .card--dark{left:630px;top:277px;background:var(--card-dark)}

  .card__brand{
    flex:0 0 170px;display:flex;align-items:center;justify-content:center;gap:14px;
  }
  .brand__mark{width:44px;height:44px;background:var(--logo-green);border-radius:4px}
  .brand__name{
    font-size:30px;line-height:1.02;font-weight:400;color:var(--logo-blue);
    text-transform:uppercase;letter-spacing:.5px;
  }
  .card--dark .brand__name{color:var(--blue-top)}

  .card__band{
    flex:1;position:relative;
    border-top:4px solid var(--green);
    background:linear-gradient(180deg,var(--blue-top) 0%,var(--blue-mid) 45%,var(--blue-deep) 100%);
    display:flex;align-items:flex-start;padding:14px 22px 0;color:var(--ink-light);
  }
  .card--light .card__band{border-top-color:#dfe8ef}

  .address{
    flex:0 0 168px;text-align:right;font-size:12.5px;line-height:1.45;padding-right:14px;
    padding-top:6px;
  }
  .address .phone{display:flex;justify-content:flex-end;align-items:center;gap:5px}
  .divider{width:1px;align-self:stretch;margin-bottom:28px;background:rgba(255,255,255,.85)}
  .person{padding-left:14px}
  .person__name{font-size:17px;font-weight:700;line-height:1.15}
  .person__title{font-size:12.5px;font-weight:700;margin-bottom:6px}
  .contact{display:flex;align-items:center;gap:7px;font-size:11px;line-height:1.6}
  .icon{width:11px;height:11px;flex:0 0 11px}
</style>
</head>
<body>

<section class="card card--light" aria-label="Business card, light version">
  <div class="card__brand">
    <span class="brand__mark"></span>
    <span class="brand__name">Keystone Pulse<br>Scan Works</span>
  </div>
  <div class="card__band">
    <div class="address">
      517 Thornbury Lane #2614<br>
      Millbrook Twp. PA. 15832<br>
      <span class="phone">724.555.0148
        <svg class="icon" viewBox="0 0 12 12"><path fill="#fff" d="M3 1l2 2.4-1 1.3a6 6 0 0 0 3.3 3.3l1.3-1L11 9l-1.2 1.8C6 10.5 1.5 6 1.2 2.2z"/></svg></span>
      <span class="phone">(800) 555-0193
        <svg class="icon" viewBox="0 0 12 12"><path fill="#fff" d="M3 1l2 2.4-1 1.3a6 6 0 0 0 3.3 3.3l1.3-1L11 9l-1.2 1.8C6 10.5 1.5 6 1.2 2.2z"/></svg></span>
    </div>
    <div class="divider"></div>
    <div class="person">
      <div class="person__name">Nora K. Pellway Hussel</div>
      <div class="person__title">President &amp; Director of Ultrasound</div>
      <div class="contact">
        <svg class="icon" viewBox="0 0 12 12"><rect x="1" y="2.5" width="10" height="7" rx="1" fill="#fff"/><path d="M1.5 3l4.5 3.5L10.5 3" stroke="#1f87d6" fill="none"/></svg>
        nora@keystonepulsescanworks.example
      </div>
      <div class="contact">
        <svg class="icon" viewBox="0 0 12 12"><circle cx="6" cy="6" r="5" fill="none" stroke="#fff"/><path d="M1 6h10M6 1c-2.5 3-2.5 7 0 10M6 1c2.5 3 2.5 7 0 10" stroke="#fff" fill="none" stroke-width=".8"/></svg>
        keystonepulsescanworks.example
      </div>
    </div>
  </div>
</section>

<section class="card card--dark" aria-label="Business card, dark version">
  <div class="card__brand">
    <span class="brand__mark"></span>
    <span class="brand__name">Keystone Pulse<br>Scan Works</span>
  </div>
  <div class="card__band">
    <div class="address">
      517 Thornbury Lane #2614<br>
      Millbrook Twp. PA. 15832<br>
      <span class="phone">724.555.0148
        <svg class="icon" viewBox="0 0 12 12"><path fill="#fff" d="M3 1l2 2.4-1 1.3a6 6 0 0 0 3.3 3.3l1.3-1L11 9l-1.2 1.8C6 10.5 1.5 6 1.2 2.2z"/></svg></span>
      <span class="phone">(800) 555-0193
        <svg class="icon" viewBox="0 0 12 12"><path fill="#fff" d="M3 1l2 2.4-1 1.3a6 6 0 0 0 3.3 3.3l1.3-1L11 9l-1.2 1.8C6 10.5 1.5 6 1.2 2.2z"/></svg></span>
    </div>
    <div class="divider"></div>
    <div class="person">
      <div class="person__name">Nora K. Pellway Hussel</div>
      <div class="person__title">President &amp; Director of Ultrasound</div>
      <div class="contact">
        <svg class="icon" viewBox="0 0 12 12"><rect x="1" y="2.5" width="10" height="7" rx="1" fill="#fff"/><path d="M1.5 3l4.5 3.5L10.5 3" stroke="#1f87d6" fill="none"/></svg>
        nora@keystonepulsescanworks.example
      </div>
      <div class="contact">
        <svg class="icon" viewBox="0 0 12 12"><circle cx="6" cy="6" r="5" fill="none" stroke="#fff"/><path d="M1 6h10M6 1c-2.5 3-2.5 7 0 10M6 1c2.5 3 2.5 7 0 10" stroke="#fff" fill="none" stroke-width=".8"/></svg>
        keystonepulsescanworks.example
      </div>
    </div>
  </div>
</section>

</body>
</html>
```